Business card design for strategy and management consulting company. Would like to have a clean and professional business card, based on the attached logo. The company is a strategy and management consulting company focusing on sustainable business modlels based on economic, social and environmental market opportunities. Preferably the logo should be included on both sides of the design.

Industry/Entity Type

Business

Contact Information for Business Card

Håvard Lilleby, CEO/Management consultant
havard.lilleby@quarvenpartners.example
Mob: +47 948 26 317
Office: Vikfjell gate 14, pb 312 sentrum, N-0172 Oslo Norway

Requirements
Must have
• Include attached logo
Nice to have
• Would like to have the logo on both sides
Should not have
• Many colours.

```html
<!DOCTYPE html>
<html lang="en">
<head>
<meta charset="utf-8">
<title>Quarven business card</title>
<link rel="stylesheet" href="https://fonts.googleapis.com/css2?family=Arimo:wght@400;700&family=Josefin+Sans:wght@300&display=swap">
<style>
  :root {
    --page: #ffffff;
    --card: #000000;
    --block: #363203;
    --ink-olive: #6e6c2c;
    --rule: #4a4826;
    --logo: #ffffff;
  }
  * { margin: 0; padding: 0; box-sizing: border-box; }
  html, body { width: 1200px; height: 1200px; overflow: hidden; background: var(--page); }
  .canvas { position: relative; width: 1200px; height: 1200px; }
  .card {
    position: absolute; left: 146px; width: 898px; height: 519px;
    background: var(--card); overflow: hidden;
    font-family: "Arimo", Arial, sans-serif; color: var(--ink-olive);
  }
  .card--front { top: 83px; }
  .card--back { top: 628px; }
  .block { position: absolute; top: 121px; width: 180px; height: 240px; background: var(--block); }
  .block--left { left: 0; }
  .block--right { right: 0; }
  .centered { position: absolute; left: 0; width: 100%; text-align: center; white-space: nowrap; }
  .person {
    position: absolute; left: 756px; transform: translateX(-50%); top: 48px;
    text-align: center; white-space: nowrap;
    font-family: "Josefin Sans", Arial, sans-serif; font-weight: 300;
  }
  .person__name { font-size: 26px; line-height: 30px; letter-spacing: 0.5px; }
  .person__role { font-size: 26px; line-height: 30px; letter-spacing: 7px; padding-left: 7px; }
  .wordmark {
    position: absolute; left: 450px; top: 206px; transform: translateX(-50%);
    white-space: nowrap;
    font-family: "Arimo", Arial, sans-serif; font-weight: 700; font-size: 66px;
    line-height: 1; color: var(--logo); letter-spacing: -1px;
  }
  .rule { position: absolute; left: 330px; width: 226px; top: 293px; height: 1px; background: var(--rule); }
  .role-line { left: -6px; top: 296px; font-size: 18px; }
  .contact { font-size: 18px; line-height: 22px; }
  .tagline { top: 302px; font-size: 19px; left: -10px; }
  .office { font-size: 22px; line-height: 26px; }
</style>
</head>
<body>
<main class="canvas">
  <section class="card card--front" aria-label="Card front">
    <div class="block block--left"></div>
    <div class="block block--right"></div>
    <div class="person">
      <p class="person__name">Håvard Lilleby</p>
      <p class="person__role">CEO</p>
    </div>
    <p class="wordmark">Quarven</p>
    <div class="rule"></div>
    <p class="centered role-line">Management Consultant</p>
    <p class="centered contact" style="top:351px">Vikfjell Gate no:14</p>
    <p class="centered contact" style="top:387px">Pb 312 Sentrum, 0172 Oslo Norway</p>
    <p class="centered contact" style="top:423px">havard.lilleby@quarvenpartners.example</p>
    <p class="centered contact" style="top:459px">mob : +47 948 26 317</p>
  </section>

  <section class="card card--back" aria-label="Card back">
    <div class="block block--left"></div>
    <div class="block block--right"></div>
    <p class="wordmark">Quarven</p>
    <p class="centered tagline">Strategy and Management Consulting Company</p>
    <p class="centered office" style="top:397px">Vikfjell Gate no:14</p>
    <p class="centered office" style="top:439px">Pb 312 Sentrum, 0172 Oslo Norway</p>
  </section>
</main>
</body>
</html>
```